Create website for home automation - Control your lighting, fans, blinds etc remotely by smartphone

Plan for SHOPIFY Website - Willowbyte Dwelling
Company name: Willowbyte Dwelling
Company Slogan: Calm Rooms Every Day
Clean, Modern, Easy to Navigate, easy to maintain - not a lot of coding. We need flash technology but displaying simply what we do.
What we provide:
We will be offering wireless switch which can be added to iOS/Android App via WiFi, allowing users to remotely turn on/off connected lights, fans, security cameras, appliances, irrigation, humidifier separately from anywhere at any time.
Control your home away from home. No more wandering of your mind on those lights or appliances which you might have left switched on. No need to drive back home to check and switch them off. Save that energy, money and time just with a click of your phone no matter how far you are from home.
Replace your home electrical switches with smart switches. They retrofit existing electrical switches and allow you to make the transformation as needed.
Easy to use and intuitive app allows you to control your lights and devices just at a click. Set any kind of ambiance suiting your occasion.
Set scenes in smartphone app to group and operate your devices just at a button click. Same device can be included in more than one scene.
Collections and Products
Light Switches
Wall Plugs
Fan Switch
Pendants etc special lighting types.
Light Dimmers
Blind Controllers
Home Page:
Home page needs to telling customers what we do and how we do it in a few words to grab people.
Logo
Phone
Email
Support – Download instructions per product
Client login
Wholesale login
Promotional video to be on home screen - this is a short 1.5 - 2 min illustration introduction video to who we are and what we do - this is yet to be created)
Social media link - Facebook
Pages:
FAQ
About Us
Support/Shipping/Returns policy
Support/Installation
Blog posts
Product pages:
Description
Price
Space for where a video will be featured - how each product works/installation.
Reviews
Our competition:
http://www.qorvat.com.au
https://brindlegadgetry.com.au/2018/04/05/best-smart-light-switches-and-plugs/
https://www.zelpinatech.com
Attachments:
Logo
Product pics
Promotional video - if ready

```html
<!DOCTYPE html>
<html lang="en">
<head>
<meta charset="utf-8">
<title>Willowbyte Dwelling – Support</title>
<link rel="stylesheet" href="https://fonts.googleapis.com/css2?family=Asap:wght@400;600;700&family=Asap+Condensed:wght@400;600&family=Tinos:wght@400;700&display=swap">
<style>
:root{
  --sun:#fde76d;
  --slate:#c3ccd3;
  --green:#3fba74;
  --panel:#b5b5b5;
  --ink:#111111;
  --white:#ffffff;
  --ocean:#1274be;
  --badge:#0b0b0b;
  --photo-dark:#3a3634;
  --photo-mid:#8a7a6a;
}
*{box-sizing:border-box;margin:0;padding:0}
html,body{width:1200px;height:2400px;overflow:hidden;background:var(--white)}
body{position:relative;font-family:"Tinos",serif;color:var(--ink)}
.abs{position:absolute}

/* hero */
.hero{left:0;top:0;width:1200px;height:395px;background:var(--sun);overflow:hidden}
.hero-slant{left:0;top:0}
.hero-photo{left:112px;top:48px;width:728px;height:347px;border-radius:180px 40px 0 0;
  background:linear-gradient(120deg,var(--photo-mid) 0%,var(--photo-dark) 60%,#1e1c1b 100%);opacity:.85}
.brand{left:144px;top:8px;width:170px;text-align:center;color:#0d2a6b;font-family:"Asap",sans-serif}
.brand-mark{display:block;width:34px;height:34px;border-radius:50%;background:#0d2a6b;margin:0 auto 4px}
.brand-name{font-size:12px;font-weight:700;letter-spacing:.3px;text-transform:uppercase}
.brand-slogan{font-size:7px;color:#0d2a6b}
.main-nav{left:312px;top:6px;display:flex;gap:19px;font-family:"Asap Condensed",sans-serif;font-size:20px;color:var(--white)}
.main-nav .current{border-bottom:4px solid var(--green);padding-bottom:2px}
.social{display:flex;gap:10px}
.social span{width:28px;height:26px;border:3px solid var(--white);border-radius:5px}
.hero-social{left:800px;top:8px}
.login{left:952px;top:6px;width:96px;height:29px;background:var(--green);color:var(--white);
  font-family:"Asap",sans-serif;font-weight:600;font-size:21px;text-align:center;line-height:29px}
.page-title{left:584px;top:182px;font-family:"Asap",sans-serif;font-weight:700;font-size:56px;color:var(--white)}

/* info blocks */
.topic-tag{width:262px;height:41px;background:var(--green);color:var(--white);text-align:center;
  font-size:20px;line-height:41px}
.topic-text{width:420px;font-size:10.6px;line-height:30px}

/* contact form */
.contact-panel{left:150px;top:771px;width:900px;height:259px;background:var(--panel)}
.field{background:var(--white);height:29px;width:454px;font-size:15px;padding:6px 4px 0}
.field-message{left:667px;top:792px;width:346px;height:216px;background:var(--white);font-size:15px;padding:10px 12px}
.send{left:397px;top:973px;width:83px;height:33px;background:var(--green);color:var(--white);font-size:15px;text-align:center;line-height:33px}

/* faq */
.faq-title{left:571px;top:1734px;font-size:33px;color:var(--green)}
.faq-title-bar{left:589px;top:1772px;width:24px;height:4px;background:var(--green)}
.faq-item{width:384px}
.faq-q{font-size:12.5px;margin-bottom:7px}
.faq-a{font-size:12.5px;line-height:14.4px}

/* footer */
.site-footer{left:0;top:2214px;width:1200px;height:186px;background:var(--ocean)}
.footer-nav{left:141px;top:2232px;display:flex;gap:38px;font-family:"Asap Condensed",sans-serif;font-weight:600;font-size:15px;color:var(--white)}
.follow{left:637px;top:2232px;font-family:"Asap",sans-serif;font-weight:700;font-size:17px;color:var(--white)}
.footer-social{left:606px;top:2251px}
.store-badge{left:618px;width:96px;height:28px;background:var(--badge);border:1px solid #666;border-radius:4px}
.foot-field{background:var(--white);font-family:"Asap",sans-serif;font-size:17px;padding:2px 4px;color:var(--ink)}
.submit{left:965px;top:2366px;width:96px;height:28px;border-radius:14px;background:var(--green);color:var(--white);
  font-family:"Asap",sans-serif;font-weight:700;font-size:19px;text-align:center;line-height:28px}
</style>
</head>
<body>

<header class="abs hero">
  <svg class="abs hero-slant" width="1200" height="395" viewBox="0 0 1200 395"><polygon points="840,395 1200,285 1200,395" fill="var(--slate)"/></svg>
  <div class="abs hero-photo" role="img" aria-label="Photo of a hand holding the receiver of a black rotary telephone"></div>
</header>

<div class="abs brand">
  <span class="brand-mark"></span>
  <div class="brand-name">Willowbyte Dwelling</div>
  <div class="brand-slogan">Calm Rooms Every Day</div>
</div>
<nav class="abs main-nav">
  <span>Home</span><span>FAQ</span><span>About Us</span><span>Support</span><span class="current">Installation</span><span>Blog</span>
</nav>
<div class="abs social hero-social"><span></span><span></span><span></span></div>
<div class="abs login">Login</div>
<h1 class="abs page-title">Support</h1>

<!-- row 1 -->
<div class="abs topic-tag" style="left:173px;top:453px">Sponsorship</div>
<div class="abs topic-tag" style="left:658px;top:453px">Media Relations</div>
<p class="abs topic-text" style="left:152px;top:500px">Lorem ipsum dolor sit amet, consectetur adipisicing elit, sed do eiusmod tempor incididunt ut labore et dolore magna aliqua. Ut enim ad minim veniam, quis nostrud exercitation ullamco laboris nisi ut aliquip ex ea commodo consequat. Duis aute irure dolor in reprehenderit in voluptate velit esse cillum dolore eu fugiat nulla pariatur. Excepteur sint occaecat cupidatat non proident, sunt in culpa qui officia deserunt mollit anim id est laborum. Sed ut perspiciatis unde omnis iste natus error sit voluptatem accusantium doloremque laudantium, totam rem aperiam, eaque ipsa quae<br>Email:hello@willowbytedwelling.com</p>
<p class="abs topic-text" style="left:638px;top:500px">Lorem ipsum dolor sit amet, consectetur adipisicing elit, sed do eiusmod tempor incididunt ut labore et dolore magna aliqua. Ut enim ad minim veniam, quis nostrud exercitation ullamco laboris nisi ut aliquip ex ea commodo consequat. Duis aute irure dolor in reprehenderit in voluptate velit esse cillum dolore eu fugiat nulla pariatur. Excepteur sint occaecat cupidatat non proident, sunt in culpa qui officia deserunt mollit anim id est laborum. Sed ut perspiciatis unde omnis iste natus error sit voluptatem accusantium doloremque laudantium, totam rem aperiam, eaque ipsa quae<br>Email:hello@willowbytedwelling.com</p>

<!-- contact form -->
<div class="abs contact-panel"></div>
<div class="abs field" style="left:186px;top:800px">Name</div>
<div class="abs field" style="left:186px;top:846px">Email</div>
<div class="abs field" style="left:186px;top:891px">Phone</div>
<div class="abs field-message">Message...</div>
<div class="abs send">Send</div>

<!-- row 2 -->
<div class="abs topic-tag" style="left:173px;top:1082px">Investor Relations</div>
<div class="abs topic-tag" style="left:658px;top:1082px">Consumer Affairs</div>
<p class="abs topic-text" style="left:152px;top:1129px">Lorem ipsum dolor sit amet, consectetur adipisicing elit, sed do eiusmod tempor incididunt ut labore et dolore magna aliqua. Ut enim ad minim veniam, quis nostrud exercitation ullamco laboris nisi ut aliquip ex ea commodo consequat. Duis aute irure dolor in reprehenderit in voluptate velit esse cillum dolore eu fugiat nulla pariatur. Excepteur sint occaecat cupidatat non proident, sunt in culpa qui officia deserunt mollit anim id est laborum. Sed ut perspiciatis unde omnis iste natus error sit voluptatem accusantium doloremque laudantium, totam rem aperiam, eaque ipsa quae<br>Email:hello@willowbytedwelling.com</p>
<p class="abs topic-text" style="left:638px;top:1129px">Lorem ipsum dolor sit amet, consectetur adipisicing elit, sed do eiusmod tempor incididunt ut labore et dolore magna aliqua. Ut enim ad minim veniam, quis nostrud exercitation ullamco laboris nisi ut aliquip ex ea commodo consequat. Duis aute irure dolor in reprehenderit in voluptate velit esse cillum dolore eu fugiat nulla pariatur. Excepteur sint occaecat cupidatat non proident, sunt in culpa qui officia deserunt mollit anim id est laborum. Sed ut perspiciatis unde omnis iste natus error sit voluptatem accusantium doloremque laudantium, totam rem aperiam, eaque ipsa quae<br>Email:hello@willowbytedwelling.com</p>

<!-- row 3 -->
<div class="abs topic-tag" style="left:173px;top:1426px">Sustainability</div>
<div class="abs topic-tag" style="left:658px;top:1426px">Environments</div>
<p class="abs topic-text" style="left:152px;top:1473px">Lorem ipsum dolor sit amet, consectetur adipisicing elit, sed do eiusmod tempor incididunt ut labore et dolore magna aliqua. Ut enim ad minim veniam, quis nostrud exercitation ullamco laboris nisi ut aliquip ex ea commodo consequat. Duis aute irure dolor in reprehenderit in voluptate velit esse cillum dolore eu fugiat nulla pariatur. Excepteur sint occaecat cupidatat non proident, sunt in culpa qui officia deserunt mollit anim id est laborum. Sed ut perspiciatis unde omnis iste natus error sit voluptatem accusantium doloremque laudantium, totam rem aperiam, eaque ipsa quae<br>Email:hello@willowbytedwelling.com</p>
<p class="abs topic-text" style="left:638px;top:1473px">Lorem ipsum dolor sit amet, consectetur adipisicing elit, sed do eiusmod tempor incididunt ut labore et dolore magna aliqua. Ut enim ad minim veniam, quis nostrud exercitation ullamco laboris nisi ut aliquip ex ea commodo consequat. Duis aute irure dolor in reprehenderit in voluptate velit esse cillum dolore eu fugiat nulla pariatur. Excepteur sint occaecat cupidatat non proident, sunt in culpa qui officia deserunt mollit anim id est laborum. Sed ut perspiciatis unde omnis iste natus error sit voluptatem accusantium doloremque laudantium, totam rem aperiam, eaque ipsa quae<br>Email:hello@willowbytedwelling.com</p>

<!-- faq -->
<h2 class="abs faq-title">FAQ</h2>
<div class="abs faq-title-bar"></div>

<div class="abs faq-item" style="left:152px;top:1806px"><p class="faq-q">Where We Invest</p><p class="faq-a">Lorem ipsum dolor sit amet, consectetur adipisicing elit, sed do eiusmod tempor incididunt ut labore et dolore magna aliqua. Ut enim ad minim veniam, quis nostrud exercitation ullamco laboris nisi ut aliquip ex ea commodo consequat. Duis aute irure dolor in reprehenderit in voluptate velit esse cillum dolore eu fugiat nulla pariatur. Excepteur sint occaecat cupidatat non proident, sunt in culpa qui officia deserunt mollit anim id est</p></div>
<div class="abs faq-item" style="left:670px;top:1806px"><p class="faq-q">Return</p><p class="faq-a">Lorem ipsum dolor sit amet, consectetur adipisicing elit, sed do eiusmod tempor incididunt ut labore et dolore magna aliqua. Ut enim ad minim veniam, quis nostrud exercitation ullamco laboris nisi ut aliquip ex ea commodo consequat. Duis aute irure dolor in reprehenderit in voluptate velit esse cillum dolore eu fugiat nulla pariatur. Excepteur sint occaecat cupidatat non proident, sunt in culpa qui officia deserunt mollit anim id est</p></div>
<div class="abs faq-item" style="left:152px;top:1961px"><p class="faq-q">What We Investt</p><p class="faq-a">Lorem ipsum dolor sit amet, consectetur adipisicing elit, sed do eiusmod tempor incididunt ut labore et dolore magna aliqua. Ut enim ad minim veniam, quis nostrud exercitation ullamco laboris nisi ut aliquip ex ea commodo consequat. Duis aute irure dolor in reprehenderit in voluptate velit esse cillum dolore eu fugiat nulla pariatur. Excepteur sint occaecat cupidatat non proident, sunt in culpa qui officia deserunt mollit anim id est</p></div>
<div class="abs faq-item" style="left:670px;top:1961px"><p class="faq-q">How Do I Invest</p><p class="faq-a">Lorem ipsum dolor sit amet, consectetur adipisicing elit, sed do eiusmod tempor incididunt ut labore et dolore magna aliqua. Ut enim ad minim veniam, quis nostrud exercitation ullamco laboris nisi ut aliquip ex ea commodo consequat. Duis aute irure dolor in reprehenderit in voluptate velit esse cillum dolore eu fugiat nulla pariatur. Excepteur sint occaecat cupidatat non proident, sunt in culpa qui officia deserunt mollit anim id est</p></div>
<div class="abs faq-item" style="left:152px;top:2116px"><p class="faq-q">Our Partners</p><p class="faq-a">Lorem ipsum dolor sit amet, consectetur adipisicing elit, sed do eiusmod tempor incididunt ut labore et dolore magna aliqua. Ut enim ad minim veniam, quis nostrud exercitation ullamco laboris nisi ut aliquip ex ea commodo consequat.</p></div>
<div class="abs faq-item" style="left:670px;top:2116px"><p class="faq-q">History</p><p class="faq-a">Lorem ipsum dolor sit amet, consectetur adipisicing elit, sed do eiusmod tempor incididunt ut labore et dolore magna aliqua. Ut enim ad minim veniam, quis nostrud exercitation ullamco laboris nisi ut aliquip ex ea commodo consequat.</p></div>

<!-- footer -->
<footer class="abs site-footer"></footer>
<nav class="abs footer-nav"><span>Home</span><span>About Us</span><span>Products</span><span>Design</span><span>Services</span><span>Contact Us</span></nav>
<div class="abs follow">Follow</div>
<div class="abs social footer-social"><span></span><span></span><span></span></div>
<div class="abs store-badge" style="top:2288px"></div>
<div class="abs store-badge" style="top:2322px"></div>
<div class="abs foot-field" style="left:733px;top:2219px;width:157px;height:24px">Name:</div>
<div class="abs foot-field" style="left:909px;top:2219px;width:157px;height:24px">Phone:</div>
<div class="abs foot-field" style="left:733px;top:2254px;width:333px;height:26px">Email</div>
<div class="abs foot-field" style="left:733px;top:2288px;width:333px;height:74px">Message:</div>
<div class="abs submit">Submit</div>

</body>
</html>
```